Business Card Design - Construction Company

Torvane Construction is in need of a sharp, modern business card design that has an architectural/high fashion feel.

We are looking for a two sided card.

One side simple dark grey/black with some texture in the background. e.g. (a mosaic of simple interconnecting shapes or a shadow of the logo.) Something to draw attention and create interest.It will need to feature a large Torvane construction logo (files attached) in metallic gradient or plain white.

The other side should contain all of our information:

(in largest text)
Name of person
Torvane Construction Pty. Ltd.

Licensed builders specialising in:
- Bathrooms
- Kitchens
- Commercial interiors

(mid sized text)
Phone number
Fax number
person@torvaneconstruction.example.au
www. torvaneconstruction.example.au

(smaller text)
ABN: 47209836512
BSA license: xxx-xxxx
PO Box 8640 Dunmore QLD 4170 (address)

Target Market(s)

professional home and business owners

Industry/Entity Type

Construction

Requirements
Must have
• Must be bold, professional looking and modern.
Nice to have
• We are undecided as to what kind of printing we will go with.
Definitely square edged.
Probably high quality satin card.
We are also interested in designs that would work well on transparent or translucent plastic.
Ideally we would print two versions.
Should not have
• Nothing with an antique feel.
No wild colours. Small amounts of colour can be good in the right place.

```html
<!DOCTYPE html>
<html lang="en">
<head>
<meta charset="utf-8">
<title>Torvane Construction – Business Card</title>
<link href="https://fonts.googleapis.com/css2?family=Source+Sans+3:wght@400&display=swap" rel="stylesheet">
<style>
  :root {
    --page-bg: #ffffff;
    --ink: #1e1e1e;
    --silver-light: #f4f4f4;
    --silver-mid: #dcdcdc;
    --silver-dark: #bdbdbd;
    --band-light: rgba(255, 255, 255, 0.55);
    --band-dark: rgba(160, 160, 160, 0.35);
    --night-light: #3a3a3a;
    --night-mid: #222222;
    --night-deep: #0e0e0e;
    --brand-ink: #f2f2f2;
    --shadow-tone: rgba(0, 0, 0, 0.18);
  }
  * { margin: 0; padding: 0; box-sizing: border-box; }
  html, body {
    width: 1200px;
    height: 900px;
    overflow: hidden;
    background: var(--page-bg);
    font-family: "Source Sans 3", "Myriad Pro", sans-serif;
    color: var(--ink);
  }
  .canvas { position: relative; width: 1200px; height: 900px; }

  /* Information side */
  .card-info {
    position: absolute;
    left: 31px; top: 281px;
    width: 484px; height: 313px;
    overflow: hidden;
    background: linear-gradient(115deg, var(--silver-mid) 0%, var(--silver-light) 45%, var(--silver-mid) 75%, var(--silver-dark) 100%);
  }
  .card-info__texture {
    position: absolute;
    inset: 0;
    background:
      linear-gradient(155deg, transparent 0%, transparent 30%, var(--band-dark) 42%, var(--band-light) 55%, var(--band-dark) 68%, transparent 80%, transparent 100%);
  }
  .identity {
    position: absolute;
    left: 15px; top: 13px;
    font-size: 21px;
    line-height: 27px;
  }
  .services {
    position: absolute;
    left: 15px; top: 86px;
    font-size: 16.6px;
    line-height: 20.3px;
    list-style: none;
  }
  .contact {
    position: absolute;
    right: 17px; top: 179px;
    text-align: right;
    font-size: 15px;
    line-height: 18.5px;
  }
  .legal {
    position: absolute;
    right: 17px; top: 263px;
    text-align: right;
    font-size: 9px;
    line-height: 12.3px;
  }

  /* Brand side */
  .card-brand {
    position: absolute;
    left: 686px; top: 281px;
    width: 484px; height: 313px;
    overflow: hidden;
    background: radial-gradient(ellipse at 50% 45%, var(--night-light) 0%, var(--night-mid) 55%, var(--night-deep) 100%);
    box-shadow: 0 10px 24px var(--shadow-tone);
  }
  .card-brand__name {
    position: absolute;
    left: 0; right: 0; top: 132px;
    text-align: center;
    font-size: 40px;
    line-height: 48px;
    color: var(--brand-ink);
  }
</style>
</head>
<body>
<main class="canvas">
  <section class="card-info">
    <div class="card-info__texture" role="img" aria-label="Large faint silver brand emblem running diagonally across the card"></div>
    <div class="identity">
      <p>Name of person</p>
      <p>Torvane Construction Pty. Ltd.</p>
    </div>
    <ul class="services">
      <li>Licensed builders specialising in:</li>
      <li>- Bathrooms</li>
      <li>- Kitchens</li>
      <li>- Commercial interiors</li>
    </ul>
    <div class="contact">
      <p>Phone number</p>
      <p>Fax number</p>
      <p>person@torvaneconstruction.example.au</p>
      <p>www. torvaneconstruction.example.au</p>
    </div>
    <div class="legal">
      <p>ABN: 47209836512</p>
      <p>BSA license: xxx-xxxx</p>
      <p>PO Box 8640 Dunmore QLD 4170 (address)</p>
    </div>
  </section>

  <section class="card-brand" role="img" aria-label="Dark textured brand side of the card with the company name">
    <p class="card-brand__name">Torvane Construction</p>
  </section>
</main>
</body>
</html>
```